Presentation Folder for A New Home Construction Company

We need a Presentation Folder for a new home construction company based in Perth, Australia. It's called Tarvo Homes and specialises in building quality homes that are affordable and people want to live in. The target market is first-home buyers.

We've rebranded the website (www.tarvohomes.com.au) and are looking to update our presentation folder to match it. We want red, white, grey and black as the colour palette, and some designs with transparent photos included but overall a minimalistic approach that aligns with our new website and vehicles.

I've attached an image of our updated car wrap, can you please follow this as a guide?

I've also attached our logo, style guide and past presentation folder for reference.

Please also include:

"Plan Well, Move In, Stay Put" - refer to the previous presentation folder.

Target Market(s)

First Home Buyers

Industry/Entity Type

New Home Construction

Font styles to use
Sans Serif
Other font styles liked:
• Monserrat

Colors
EB3D1F
EC4F4E
F09395
F8D3D4
FCEDEE

Requirements
Must have
• Monserrat or Open Sans Font and Include the colours from the attached brand guide, the contact details and address,
Nice to have
• some with a photo feature - but not the main component, very minimal.
Should not have
• Too many elements, (refer to previous folder attachment) animations or graphics.

```html
<!DOCTYPE html>
<html lang="en">
<head>
<meta charset="utf-8">
<title>Tarvo Homes – Presentation Folder</title>
<link href="https://fonts.googleapis.com/css2?family=Poppins:wght@400;500;600;700;800&display=swap" rel="stylesheet">
<style>
  :root {
    --red: #e31e26;
    --red-deep: #b7161c;
    --grey-dark: #55565a;
    --grey-flap: #5d5e62;
    --grey-text: #333436;
    --panel: #f1f1f2;
    --panel-light: #f8f8f8;
    --white: #ffffff;
  }
  * { margin: 0; padding: 0; box-sizing: border-box; }
  html, body { width: 750px; height: 1200px; overflow: hidden; }
  body {
    background: var(--white);
    font-family: "Poppins", sans-serif;
    color: var(--grey-text);
    position: relative;
  }
  .folder { position: absolute; left: 0; top: 0; width: 750px; height: 1200px; }

  .side-flap {
    position: absolute; left: 25px; top: 339px; width: 106px; height: 411px;
    background: linear-gradient(180deg, #66676b 0%, var(--grey-flap) 100%);
    border-top-left-radius: 16px;
  }
  .main-panel {
    position: absolute; left: 130px; top: 339px; width: 595px; height: 411px;
    background: linear-gradient(180deg, var(--panel-light) 0%, var(--panel) 100%);
  }
  .house-photo {
    position: absolute; left: 165px; top: 0; width: 430px; height: 411px;
    background: linear-gradient(160deg, rgba(255,255,255,0) 0%, rgba(200,200,202,0.45) 45%, rgba(170,170,172,0.5) 100%);
  }
  .red-band {
    position: absolute; left: 614px; top: 367px; width: 83px; height: 383px;
    background: linear-gradient(180deg, var(--red) 0%, #d21c23 55%, var(--red-deep) 100%);
  }
  .bottom-flap {
    position: absolute; left: 130px; top: 750px; width: 290px; height: 112px;
  }

  .portrait {
    position: absolute; left: 130px; top: 536px; width: 117px; height: 214px;
    background: linear-gradient(180deg, #d9c7b8 0%, #b9a090 28%, #4f5b6d 45%, #3d4858 100%);
    border-top-left-radius: 40px; border-top-right-radius: 50px;
  }

  .brand { position: absolute; left: 455px; top: 378px; }
  .brand-name {
    display: flex; align-items: center; gap: 5px;
    font-weight: 700; font-size: 18px; line-height: 1.1; color: var(--grey-dark);
    white-space: nowrap;
  }
  .brand-name .mark { width: 8px; height: 8px; background: var(--red); flex: none; }
  .brand-line {
    margin-top: 6px; font-weight: 500; font-size: 7px; letter-spacing: 1.2px;
    color: var(--grey-dark); white-space: nowrap;
  }

  .headline {
    position: absolute; left: 455px; top: 528px;
    font-weight: 700; font-size: 27px; line-height: 1.12; color: var(--grey-dark);
    letter-spacing: -0.3px;
  }
  .headline .accent { color: var(--red); }

  .web { position: absolute; font-size: 9.5px; letter-spacing: 0.6px; color: var(--grey-text); white-space: nowrap; }
  .web b { color: var(--red); font-weight: 700; }
  .web-front { left: 456px; top: 706px; }
  .web-back { left: 263px; top: 706px; }

  .director { position: absolute; left: 262px; top: 538px; width: 150px; }
  .director-name { font-weight: 500; font-size: 13px; color: var(--red); }
  .director-role { font-weight: 500; font-size: 5.5px; color: var(--grey-text); margin-top: 1px; }
  .intro { margin-top: 14px; font-size: 5.9px; line-height: 1.25; width: 150px; }
  .years { display: flex; align-items: center; gap: 4px; margin-top: 4px; color: var(--red); }
  .years .for { font-size: 7px; line-height: 0.9; color: var(--grey-text); }
  .years .num { font-weight: 700; font-size: 19px; line-height: 1; }
  .years .unit { font-weight: 700; font-size: 12px; align-self: flex-end; margin-bottom: 1px; }
  .contacts { list-style: none; margin-top: 7px; font-size: 5.9px; line-height: 1.25; }
  .contacts li { display: flex; gap: 4px; margin-bottom: 4px; }
  .contacts svg { width: 6px; height: 6px; flex: none; margin-top: 0.5px; }
</style>
</head>
<body>
<div class="folder">
  <div class="side-flap" role="img" aria-label="Faint tree and house photograph on grey pocket flap"></div>

  <div class="main-panel">
    <div class="house-photo" role="img" aria-label="Faded photograph of a modern two-storey home"></div>
  </div>

  <div class="red-band" role="img" aria-label="Red-tinted photograph of a home facade"></div>

  <svg class="bottom-flap" viewBox="0 0 290 112" role="img" aria-label="Red-tinted photograph on pocket flap">
    <defs>
      <linearGradient id="flapFill" x1="0" y1="0" x2="0" y2="1">
        <stop offset="0" stop-color="#e31e26"/>
        <stop offset="1" stop-color="#c3181f"/>
      </linearGradient>
    </defs>
    <path d="M0 0 H290 V72 Q290 112 250 112 H70 L35 78 L22 82 L10 68 L22 54 L0 32 Z" fill="url(#flapFill)"/>
    <g transform="rotate(180 145 50)">
      <text x="145" y="38" text-anchor="middle" font-family="Poppins, sans-serif" font-size="9" letter-spacing="0.6" fill="#ffffff">www.tarvohomes.com.au</text>
      <text x="145" y="62" text-anchor="middle" font-family="Poppins, sans-serif" font-weight="700" font-size="16" fill="#ffffff">Tarvo Homes</text>
    </g>
  </svg>

  <div class="portrait" role="img" aria-label="Photograph of the managing director leaning on a tablet"></div>

  <div class="brand">
    <div class="brand-name"><span>Tarvo Homes</span><span class="mark"></span></div>
    <p class="brand-line">FIRST HOMES BY DARREN HOLT</p>
  </div>

  <h1 class="headline">PLAN WELL<br>MOVE IN<br><span class="accent">STAY PUT</span></h1>

  <p class="web web-front">www.<b>tarvohomes</b>.com.au</p>

  <section class="director">
    <p class="director-name">Darren Holt</p>
    <p class="director-role">Managing director</p>
    <p class="intro">Offering first home buyers the same outstanding service &amp; innovation that has been Darren Holt’s hallmark</p>
    <div class="years">
      <span class="for">FOR<br>OVER</span>
      <span class="num">15</span>
      <span class="unit">YEARS</span>
    </div>
    <ul class="contacts">
      <li>
        <svg viewBox="0 0 10 10"><path d="M2 1 L4 3 L3 4 Q4 6 6 7 L7 6 L9 8 L8 9.5 Q3 9 0.5 2 Z" fill="#e31e26"/></svg>
        <span>08 9000 4121</span>
      </li>
      <li>
        <svg viewBox="0 0 10 10"><rect x="2.5" y="1" width="5" height="3" fill="#e31e26"/><rect x="1" y="4" width="8" height="4" rx="1" fill="#e31e26"/><rect x="2.5" y="7" width="5" height="2.5" fill="#e31e26"/></svg>
        <span>08 9000 4122</span>
      </li>
      <li>
        <svg viewBox="0 0 10 10"><rect x="0.5" y="2" width="9" height="6" fill="#e31e26"/><path d="M0.5 2 L5 5.5 L9.5 2" fill="none" stroke="#ffffff" stroke-width="0.8"/></svg>
        <span>enquiries@tarvohomes.com.au</span>
      </li>
      <li>
        <svg viewBox="0 0 10 10"><path d="M5 10 L1.8 5 A3.6 3.6 0 1 1 8.2 5 Z" fill="#e31e26"/><circle cx="5" cy="3.6" r="1.3" fill="#ffffff"/></svg>
        <span>41 Kestrel Road, Balcatta,<br>Western Australia 6021 PO Box 318,<br>Balcatta WA 6914</span>
      </li>
    </ul>
  </section>

  <p class="web web-back">www.<b>tarvohomes</b>.com.au</p>
</div>
</body>
</html>
```